lanternox munchies snack packaging

We are a new startup snack company that need a design for a snack packaging. Our snack goes by the name of lanternox munchies. Its a traditional snack usually eaten during festive seasons in south east asia region. The idea is to revolutionize the notion of the snack from one that is eaten during these celebratory seasons to an everyday one. The packaging design should be modern and minimalist yet fun too, also taking into consideration that it should not appear to be too childish. It should stand out from the other snacks products like potato chips etc if placed on the same shelf. The colour scheme is not decided yet as we are open to more ideas but colours should be complementary and not more than 2 or 3 hopefully. There should be also be an enthic sense of south east asian features on the design and it should reflects the Chinese, Malay and indian heritage. It need not be too obvious, a subtle kind should suffice. The packaging should also have the particular graphic/shape of the mould that i have upload followed by the picture of the snack. I have included a mock up of the logo of my company. Proposed designs can feel free to alter the lanternox graphic to a more modern, minimalist yet whimsical and fun. Proposed designs should have a front and back view of the packaging. We are looking to launch at 4 to 5 flavours like white sesame, black sesame, peanuts with white sesame and original.
Updates

Project Deadline Extended
Reason: Not enough submissions coming in yet.

Project Deadline Extended
Reason: Extension of deadline to allow more designs to come in.

Target Market(s)

All ages from as young as 5 to 6 years old to 60 to 70s.

Industry/Entity Type

It Company

Font styles to use
Other font styles liked:
• Fonts should be simple and minimalist. Easy for elderly to read without straining the eyes.

Requirements
Must have
• My logo which I have designed. Designers can feel free to tweak and enhance the design of the logo. The colour is not definite yet. Consumers must know what
• we are selling from the design of the packaging without guessing how it look
• like. The suggested packaging dimension is 17cm (W) by 23.5cm (H).
Nice to have
• We are looking to print the package using kraft paper which I have attached.
Should not have
• religious inclination of motifs, logo etc.

```html
<!DOCTYPE html>
<html lang="en">
<head>
<meta charset="utf-8">
<title>lanternox munchies – Sesame Black pouch</title>
<link rel="stylesheet" href="https://fonts.googleapis.com/css2?family=Josefin+Sans:wght@300;400&family=Quicksand:wght@400;700&display=swap">
<style>
  :root {
    --backdrop: #e4e3e1;
    --kraft-light: #d6ae80;
    --kraft: #c99b68;
    --kraft-dark: #b88a55;
    --brand-red: #b3212a;
    --brand-red-deep: #9c1a22;
    --ink: #1a1410;
    --paper-white: #ffffff;
  }
  * { margin: 0; padding: 0; box-sizing: border-box; }
  html, body {
    width: 1200px; height: 900px; overflow: hidden;
    background: var(--backdrop);
  }
  .pouch {
    position: absolute; left: 370px; top: 70px;
    width: 504px; height: 758px;
    background: linear-gradient(180deg, var(--kraft-light) 0%, var(--kraft) 55%, var(--kraft-dark) 100%);
    border-radius: 6px 6px 4px 4px;
    overflow: hidden;
  }
  .top-band {
    position: absolute; left: 0; right: 0; top: 6px; height: 12px;
    background: var(--brand-red);
  }
  .brand-tab {
    position: absolute; left: 132px; top: 0; width: 232px; height: 380px;
  }
  .brand-tab svg { position: absolute; inset: 0; }
  .brand-dot {
    position: absolute; left: 56px; top: 42px; width: 120px; height: 120px;
    background: var(--paper-white); border-radius: 50%;
  }
  .brand-name, .brand-sub {
    position: absolute; left: 0; width: 232px;
    text-align: center; color: var(--paper-white);
    font-family: "Quicksand", sans-serif; font-weight: 700;
    line-height: 1;
  }
  .brand-name { top: 200px; font-size: 40px; letter-spacing: -0.5px; }
  .brand-sub { top: 244px; font-size: 30px; }
  .flavour {
    position: absolute; left: 0; right: 0; top: 398px;
    text-align: center; color: var(--ink);
    font-family: "Josefin Sans", sans-serif; font-weight: 400;
    font-size: 50px; line-height: 1; letter-spacing: 0;
  }
  .net-weight {
    position: absolute; left: 0; right: 0; top: 580px;
    text-align: center; color: var(--brand-red);
    font-family: "Quicksand", sans-serif; font-weight: 400;
    font-size: 21px; line-height: 1;
  }
  .pattern-band {
    position: absolute; left: 40px; right: 12px; top: 624px; height: 74px;
    background: linear-gradient(180deg, var(--brand-red) 0%, var(--brand-red-deep) 50%, var(--brand-red) 100%);
  }
  .bottom-band {
    position: absolute; left: 0; right: 0; top: 714px; height: 16px;
    background: var(--brand-red);
  }
</style>
</head>
<body>
  <div class="pouch">
    <div class="top-band"></div>
    <div class="brand-tab">
      <svg width="232" height="380" viewBox="0 0 232 380">
        <path d="M0 0 H232 V320 Q116 405 0 320 Z" fill="var(--brand-red)"/>
        <path d="M54 336 Q116 366 178 336" fill="none" stroke="var(--paper-white)" stroke-width="2.5" stroke-linecap="round"/>
      </svg>
      <div class="brand-dot"></div>
      <div class="brand-name">lanternox</div>
      <div class="brand-sub">munchies</div>
    </div>
    <h1 class="flavour">SESAME BLACK</h1>
    <p class="net-weight">Net Weight. 70 gram</p>
    <div class="pattern-band" role="img" aria-label="Border of repeating red mould-shaped ornaments"></div>
    <div class="bottom-band"></div>
  </div>
</body>
</html>
```